Commercial Construction Interior Fitout company needs Logo and Business Cards

We need a logo and business card design. We specialise in Commercial Ceilings, Partitions, Plastering and Carpentry.

Company name: 7QX Commercial Interiors. Would like a professional looking card more than a fancy look. Gloss front preferably black pattern with Fluro Green and white text.

Will need:

Name
Position
Phone
Fax
Email
Postal Address
Web address
Updates

Thank you so much everyone for your efforts and fantastic designs..   If I didn't respond to everyone personally,  my apologises. 

Again, thanks all

R.M                               

Target Market(s)

Existing & New clients in the Construction Industry

Industry/Entity Type

Business

Requirements
Nice to have
• 7QX to be overlapped or made into some sort of Logo

```html
<!DOCTYPE html>
<html lang="en">
<head>
<meta charset="utf-8">
<title>7QX Commercial Interiors – Business Card</title>
<link href="https://fonts.googleapis.com/css2?family=Questrial&display=swap" rel="stylesheet">
<style>
  :root {
    --page: #ffffff;
    --card-top: #2a2b2d;
    --card-bottom: #161718;
    --fluro: #6fd43a;
    --fluro-deep: #2fae3a;
    --fluro-light: #c8ef3c;
    --ink: #f2f2f2;
    --ink-soft: #d8d8d8;
    --rule: #8a8a8a;
  }
  * { margin: 0; padding: 0; box-sizing: border-box; }
  html, body { width: 1200px; height: 900px; overflow: hidden; background: var(--page); }
  body { position: relative; font-family: "Questrial", "Century Gothic", sans-serif; }

  .card {
    position: absolute;
    top: 332px;
    width: 572px;
    height: 353px;
    background: linear-gradient(180deg, var(--card-top) 0%, var(--card-bottom) 100%);
    color: var(--ink);
  }
  .card--front { left: 16px; }
  .card--back { left: 608px; }

  /* front */
  .brand {
    position: absolute;
    left: 30px;
    top: 36px;
    display: flex;
    align-items: center;
    gap: 22px;
  }
  .brand__mark {
    width: 76px;
    height: 76px;
    background: var(--fluro);
  }
  .brand__name {
    font-size: 27px;
    color: var(--ink-soft);
    letter-spacing: 0.5px;
  }
  .accent-band {
    position: absolute;
    left: 0; right: 0;
    top: 176px;
    height: 4px;
    background: linear-gradient(90deg, var(--fluro-deep), var(--fluro-light) 50%, var(--fluro-deep));
  }
  .person {
    position: absolute;
    right: calc(572px - 222px);
    top: 214px;
    text-align: right;
  }
  .person__name { font-size: 18px; color: var(--fluro); }
  .person__role { font-size: 14px; color: var(--ink); margin-top: 3px; }
  .divider {
    position: absolute;
    left: 247px;
    top: 196px;
    width: 1px;
    height: 118px;
    background: var(--rule);
  }
  .contacts {
    position: absolute;
    left: 270px;
    top: 200px;
    list-style: none;
    font-size: 15px;
    line-height: 20px;
  }
  .contacts li { display: flex; align-items: flex-start; gap: 4px; }
  .contacts svg { width: 16px; height: 16px; margin-top: 2px; flex: none; fill: var(--fluro); }
  .contacts .indent { padding-left: 20px; }

  /* back */
  .emblem {
    position: absolute;
    left: 50%;
    top: 48px;
    width: 130px;
    height: 130px;
    margin-left: -65px;
    background: var(--fluro);
  }
  .back-name {
    position: absolute;
    left: 0; right: 0;
    top: 290px;
    text-align: center;
    font-size: 27px;
    color: var(--ink-soft);
    letter-spacing: 0.5px;
  }
</style>
</head>
<body>

<section class="card card--front">
  <div class="brand">
    <span class="brand__mark"></span>
    <span class="brand__name">7QX Commercial Interiors</span>
  </div>
  <div class="accent-band"></div>

  <div class="person">
    <p class="person__name">Dana Hollis</p>
    <p class="person__role">Manager</p>
  </div>
  <div class="divider"></div>

  <ul class="contacts">
    <li>
      <svg viewBox="0 0 16 16" aria-hidden="true"><path d="M3.5 1.5l2.5 3-1.5 1.8c.9 1.9 2.3 3.3 4.2 4.2l1.8-1.5 3 2.5-1.4 2.4C7 13.5 2.5 9 1.1 2.9z"/></svg>
      <span>719-555-0184</span>
    </li>
    <li>
      <svg viewBox="0 0 16 16" aria-hidden="true"><path d="M4 1h6l2 2v3H4zM2 7h12v7H2zm2 2v1h2V9zm4 0v1h2V9zm-4 2v1h2v-1zm4 0v1h2v-1z"/></svg>
      <span>719-555-0162</span>
    </li>
    <li>
      <svg viewBox="0 0 16 16" aria-hidden="true"><path d="M1 4h14v9H1zm1.5 1.2L8 9l5.5-3.8V5h-11z"/></svg>
      <span>7qxcommercial@mailbox.com</span>
    </li>
    <li>
      <svg viewBox="0 0 16 16" aria-hidden="true"><path d="M8 1a7 7 0 100 14A7 7 0 008 1zm0 1.3c.8.8 1.5 2.3 1.7 4.2H6.3C6.5 4.6 7.2 3.1 8 2.3zM2.4 7.5h2.6c.1 1.2.3 2.3.7 3.2H3.2a5.7 5.7 0 01-.8-3.2zm0-1A5.7 5.7 0 013.2 4.3h2.5c-.4.9-.6 1.9-.7 2.2zm4 1h3.3c-.1 1.2-.4 2.3-.8 3.2H7.2c-.5-.9-.8-2-.8-3.2zm4.3 0h2.9a5.7 5.7 0 01-.8 3.2h-2.5c.3-.9.5-2 .4-3.2zm0-1c0-.3-.2-1.3-.5-2.2h2.5c.5.7.7 1.4.8 2.2zM8 13.7c-.5-.5-.9-1.1-1.2-2h2.4c-.3.9-.7 1.5-1.2 2z"/></svg>
      <span>www.7qxcommercial.com</span>
    </li>
    <li>
      <svg viewBox="0 0 16 16" aria-hidden="true"><path d="M8 1.5L.8 8h2.2v6.5h3.8v-4h2.4v4h3.8V8h2.2z"/></svg>
      <span>4800 N. Ridgeline Road,</span>
    </li>
    <li class="indent"><span>Ridgeview, CO 80999</span></li>
  </ul>
</section>

<section class="card card--back">
  <span class="emblem"></span>
  <p class="back-name">7QX Commercial Interiors</p>
</section>

</body>
</html>
```